I am looking for a modern style design for a podcast cover art.
Titled: Open Horizon with R.T. Pellow
colors to stay in the grays, reds, blacks, white, gold, and maybe blues if it fits well. I attached a mock up of what we are going for and a current podcast cover we drew inspiration from.
Colors
3276b5
ec1f27
f04a50
1b1b1b
474747
919191
d2d2d2

```html
<!DOCTYPE html>
<html lang="en">
<head>
<meta charset="utf-8">
<title>Open Horizon with R.T. Pellow — Podcast Cover</title>
<link rel="stylesheet" href="https://fonts.googleapis.com/css2?family=Montserrat:wght@300;700;800&display=swap">
<style>
  :root {
    --page: #ffffff;
    --panel-dark: #1b1b1b;
    --panel-mid: #474747;
    --gray: #919191;
    --light: #d2d2d2;
    --white: #ffffff;
    --red: #ec1f27;
    --gold: #c9a45c;
    --square-red: #8a2a2c;
    --square-rust: #5a2a1c;
    --square-deep: #4a0d10;
  }
  * { margin: 0; padding: 0; box-sizing: border-box; }
  html, body {
    width: 1200px;
    height: 692px;
    overflow: hidden;
    background: var(--page);
  }
  .cover {
    position: relative;
    width: 1200px;
    height: 692px;
  }
  .cover-art {
    position: absolute;
    left: 42px;
    top: 42px;
    width: 1116px;
    height: 608px;
    overflow: hidden;
    background: radial-gradient(ellipse at 45% 35%, var(--panel-mid) 0%, #2e2e2e 45%, var(--panel-dark) 100%);
  }
  .decor {
    position: absolute;
    inset: 0;
  }
  .host-photo {
    position: absolute;
    left: 840px;
    top: 88px;
    width: 276px;
    height: 520px;
    background: linear-gradient(160deg, #cfcfcf 0%, #8a8a8a 22%, #2a2a2a 45%, #111111 100%);
  }
  .title {
    position: absolute;
    left: 130px;
    top: 190px;
    width: 470px;
    text-align: center;
    font-family: "Montserrat", sans-serif;
    line-height: 1;
  }
  .title-top {
    display: block;
    font-weight: 700;
    font-size: 70px;
    letter-spacing: 8px;
    color: var(--white);
    text-shadow: 0 2px 6px rgba(0,0,0,.6);
  }
  .title-main {
    display: block;
    margin-top: 22px;
    font-weight: 800;
    font-size: 86px;
    letter-spacing: 2px;
    color: var(--red);
    text-shadow: 0 2px 6px rgba(0,0,0,.6);
  }
  .accent { color: var(--gold); }
  .host-line {
    position: absolute;
    left: 136px;
    top: 528px;
    font-family: "Montserrat", sans-serif;
    font-weight: 300;
    font-size: 34px;
    letter-spacing: 4px;
    color: var(--gray);
  }
</style>
</head>
<body>
<div class="cover">
  <div class="cover-art">
    <svg class="decor" width="1116" height="608" viewBox="0 0 1116 608" aria-hidden="true">
      <rect x="23" y="30" width="108" height="106" fill="var(--square-rust)" opacity=".7"/>
      <rect x="618" y="58" width="152" height="158" fill="var(--square-red)" opacity=".65"/>
      <rect x="773" y="0" width="155" height="55" fill="var(--square-red)" opacity=".55"/>
      <rect x="106" y="421" width="102" height="105" fill="var(--square-rust)" opacity=".75"/>
      <rect x="0" y="470" width="153" height="138" fill="var(--square-rust)" opacity=".45"/>
      <rect x="630" y="430" width="170" height="170" fill="var(--square-rust)" opacity=".6" transform="rotate(12 715 515)"/>
    </svg>
    <div class="host-photo" role="img" aria-label="Black and white photo of the host in a tuxedo and bow tie, pointing toward the title"></div>
    <svg class="decor" width="1116" height="608" viewBox="0 0 1116 608" aria-hidden="true">
      <rect x="960" y="40" width="170" height="220" fill="var(--square-deep)" opacity=".7" transform="rotate(-8 1045 150)"/>
      <rect x="955" y="430" width="150" height="150" fill="var(--square-red)" opacity=".7" transform="rotate(-14 1030 505)"/>
    </svg>
    <h1 class="title">
      <span class="title-top">OP<span class="accent">E</span>N</span>
      <span class="title-main">HOR<span class="accent">I</span>ZON</span>
    </h1>
    <p class="host-line">with R.T. PELLOW</p>
  </div>
</div>
</body>
</html>
```